" Dentista, especialista em Ortodontia. Professor Universitário, com titulaçao de excelência (Doutor). Atua em consultório particular atuando em uma odontologia de excelência, correçao dos dentes através de aparelhos dentários e reabilitaçao oral com técnicas de altíssimo nível em um ambiente diferenciado. Profissional qualificado e bem conceituado no mercado de trabalho. Possui uma logo, feita por um amador, a qual tive a infelicidade de descobrir que foi clonada de um profissional americano. "

```html
<!DOCTYPE html>
<html lang="pt-BR">
<head>
<meta charset="UTF-8">
<title>Dr. Renato Valença — Envelopes</title>
<link href="https://fonts.googleapis.com/css2?family=Montserrat:wght@400;700&display=swap" rel="stylesheet">
<style>
  :root {
    --teal: #46a8ad;
    --teal-dark: #3a959a;
    --teal-shadow: #34878c;
    --paper: #ffffff;
    --paper-shade: #eef0f1;
    --navy: #1f4e78;
    --backdrop: #e7e4df;
  }
  html, body {
    margin: 0;
    width: 1200px;
    height: 1200px;
    overflow: hidden;
    background: var(--backdrop);
    font-family: "Montserrat", Arial, sans-serif;
  }
  .stage {
    position: relative;
    width: 1200px;
    height: 1200px;
  }
  /* Front envelope */
  .envelope-front {
    position: absolute;
    left: 120px;
    top: 130px;
    width: 440px;
    height: 985px;
  }
  .envelope-front .flap-edge {
    position: absolute;
    left: 0; top: 0;
    width: 440px; height: 985px;
    background: var(--teal);
  }
  .envelope-front .face {
    position: absolute;
    left: 0; top: 22px;
    width: 426px; height: 963px;
    background: linear-gradient(160deg, var(--paper) 55%, var(--paper-shade));
    box-shadow: 0 6px 18px rgba(0,0,0,0.18);
  }
  .brand {
    position: absolute;
    left: 70px;
    top: 800px;
  }
  .brand-row {
    display: flex;
    align-items: center;
    gap: 12px;
  }
  .brand-dot {
    width: 30px; height: 30px;
    border-radius: 50%;
    background: var(--teal);
  }
  .brand-name {
    font-weight: 700;
    font-size: 30px;
    color: var(--navy);
    letter-spacing: -0.3px;
    white-space: nowrap;
  }
  .brand-role {
    margin-top: 4px;
    margin-left: 42px;
    font-size: 15px;
    letter-spacing: 7px;
    color: var(--teal);
  }
  /* Back envelope */
  .envelope-back {
    position: absolute;
    left: 630px;
    top: 145px;
    width: 450px;
    height: 960px;
    background: var(--teal);
    box-shadow: 0 6px 18px rgba(0,0,0,0.18);
  }
  .envelope-back svg.flap {
    position: absolute;
    left: 0; top: 0;
  }
  .back-info {
    position: absolute;
    left: 40px;
    top: 745px;
    color: #ffffff;
    font-size: 12px;
    line-height: 1.45;
  }
  .back-info .brand-row { gap: 8px; }
  .back-info .brand-dot {
    width: 14px; height: 14px;
    background: #ffffff;
  }
  .back-info .brand-name {
    color: #ffffff;
    font-size: 14px;
  }
  .back-info .brand-role {
    margin: 0 0 8px 22px;
    font-size: 8px;
    letter-spacing: 3px;
    color: #ffffff;
  }
  .back-info address {
    font-style: normal;
  }
</style>
</head>
<body>
<main class="stage">
  <section class="envelope-front">
    <div class="flap-edge"></div>
    <div class="face">
      <div class="brand">
        <div class="brand-row">
          <span class="brand-dot"></span>
          <span class="brand-name">Dr. Renato Valença</span>
        </div>
        <div class="brand-role">ORTODONTISTA</div>
      </div>
    </div>
  </section>

  <section class="envelope-back">
    <svg class="flap" width="450" height="240" viewBox="0 0 450 240">
      <polygon points="0,0 450,0 450,8 225,200 0,8" fill="var(--teal-dark)"/>
      <polyline points="0,8 225,200 450,8" fill="none" stroke="var(--teal-shadow)" stroke-width="2"/>
    </svg>
    <div class="back-info">
      <div class="brand-row">
        <span class="brand-dot"></span>
        <span class="brand-name">Dr. Renato Valença</span>
      </div>
      <div class="brand-role">ORTODONTISTA</div>
      <address>
        Rua das Acácias, 120 - Sala 4<br>
        Campinas - SP<br>
        11 4000-1234 / 4000-5678
      </address>
    </div>
  </section>
</main>
</body>
</html>
```